Finanical service company needs a Pull up Banner

We need a pull up banner for a financial service company bases in Sydney called HALVEN FX. Our products include: Foreign currency pairs, mentals, oil, indices. Clients can trade our products through Qorvex, Android, online platform. We would like to see designs feel global , easy access and financial freedom.

```html
<!DOCTYPE html>
<html lang="en">
<head>
<meta charset="utf-8">
<title>HALVEN FX – Pull Up Banner</title>
<link rel="stylesheet" href="https://fonts.googleapis.com/css2?family=Josefin+Sans:wght@700&family=Source+Sans+3:wght@400;600;700&display=swap">
<style>
  :root {
    --purple: #4a2585;
    --orange: #e5411f;
    --hero-dark: #1d1630;
    --hero-mid: #2c2050;
    --footer: #323844;
    --ink: #1e1e1e;
    --white: #ffffff;
  }
  * { margin: 0; padding: 0; box-sizing: border-box; }
  html, body { width: 674px; height: 1200px; overflow: hidden; background: var(--white); }
  .banner {
    position: relative;
    width: 674px;
    height: 1200px;
    overflow: hidden;
    background: var(--white);
    font-family: "Source Sans 3", sans-serif;
    color: var(--ink);
  }
  .shapes { position: absolute; inset: 0; width: 674px; height: 1200px; }

  .brand {
    position: absolute;
    top: 42px;
    left: 0;
    width: 674px;
    display: flex;
    justify-content: center;
    align-items: center;
    gap: 16px;
  }
  .brand-mark { width: 40px; height: 40px; background: var(--orange); }
  .brand-name {
    font-family: "Josefin Sans", sans-serif;
    font-weight: 700;
    font-size: 60px;
    line-height: 1;
    color: var(--purple);
    letter-spacing: 1px;
    padding-top: 8px;
  }

  .values {
    position: absolute;
    top: 262px;
    left: 0;
    width: 674px;
    text-align: center;
    list-style: none;
    color: var(--white);
    font-family: "Josefin Sans", sans-serif;
    font-weight: 700;
    font-size: 50px;
    line-height: 1;
  }
  .values li { height: 56px; padding-top: 10px; }
  .values .divider {
    height: 58px;
    display: flex;
    justify-content: center;
    align-items: center;
  }
  .values .divider span { width: 48px; height: 3px; background: var(--white); }

  .intro {
    position: absolute;
    top: 744px;
    left: 50px;
    width: 574px;
    text-align: center;
    font-size: 22px;
    line-height: 31px;
    letter-spacing: -0.2px;
  }
  .intro p + p { margin-top: 31px; }
  .highlight { color: var(--orange); font-weight: 600; }

  .contact {
    position: absolute;
    top: 1026px;
    left: 39px;
    color: var(--white);
    font-size: 14px;
    line-height: 1.3;
  }
  .contact-label { font-size: 14px; letter-spacing: 0.3px; }
  .contact-company { font-size: 19px; font-weight: 700; letter-spacing: 0.5px; margin-bottom: 8px; }
  .contact-list { list-style: none; }
  .contact-list li { display: flex; gap: 8px; align-items: flex-start; margin-bottom: 7px; }
  .contact-list svg { width: 14px; height: 14px; flex: none; margin-top: 2px; }

  .website {
    position: absolute;
    top: 1112px;
    left: 0;
    width: 674px;
    height: 42px;
  }
  .website-text {
    position: absolute;
    top: 0;
    right: 22px;
    line-height: 42px;
    color: var(--white);
    font-size: 19px;
    letter-spacing: 1.5px;
  }
</style>
</head>
<body>
<div class="banner">
  <svg class="shapes" viewBox="0 0 674 1200" aria-hidden="true">
    <defs>
      <linearGradient id="heroTone" x1="0" y1="0" x2="1" y2="1">
        <stop offset="0" stop-color="var(--hero-mid)"/>
        <stop offset="0.55" stop-color="var(--hero-dark)"/>
        <stop offset="1" stop-color="#3a2a6e"/>
      </linearGradient>
    </defs>
    <!-- hero accents -->
    <polygon points="0,225 335,149 335,176" fill="var(--purple)"/>
    <polygon points="150,209 559,137 559,164" fill="var(--orange)"/>
    <!-- hero footer accents -->
    <polygon points="232,630 674,682 232,666" fill="var(--orange)"/>
    <polygon points="402,671 674,682 402,694" fill="var(--purple)"/>
    <!-- footer band -->
    <polygon points="0,973 674,1062 674,1200 0,1200" fill="var(--footer)"/>
    <polygon points="186,973 674,1062 200,999" fill="var(--orange)"/>
    <!-- website tab -->
    <polygon points="420,1112 674,1112 674,1154 402,1154" fill="var(--orange)"/>
  </svg>

  <svg class="shapes" viewBox="0 0 674 1200" role="img" aria-label="Dark purple photograph of a trading chart on a screen">
    <polygon points="0,225 674,151 674,681 0,607" fill="url(#heroTone)"/>
  </svg>

  <header class="brand">
    <span class="brand-mark"></span>
    <span class="brand-name">HALVEN FX</span>
  </header>

  <ul class="values">
    <li>COLLABORATIVE</li>
    <li class="divider"><span></span></li>
    <li>LEADING</li>
    <li class="divider"><span></span></li>
    <li>PROFESSIONAL</li>
  </ul>

  <section class="intro">
    <p><span class="highlight">HALVEN FX</span> is a leading forex broker in Australia, which provides professional services to retail and institutional customers in online investing and trading.</p>
    <p><span class="highlight">The product ranges</span> include CFD's over forex, precious metals, crude oil, global indices and related financial derivative instruments.</p>
  </section>

  <footer class="contact">
    <p class="contact-label">CONTACT US</p>
    <p class="contact-company">HALVEN FX PTY LTD</p>
    <ul class="contact-list">
      <li>
        <svg viewBox="0 0 14 14"><path d="M7 13s-4.5-4.6-4.5-7.5a4.5 4.5 0 0 1 9 0C11.5 8.4 7 13 7 13z" fill="none" stroke="var(--orange)" stroke-width="1.2"/><circle cx="7" cy="5.5" r="1.6" fill="none" stroke="var(--orange)" stroke-width="1.2"/></svg>
        <span>Level 9, Harbourline 40 Market Street<br>Sydney, NSW 2000 Australia</span>
      </li>
      <li>
        <svg viewBox="0 0 14 14"><path d="M3 1.5l2.3 2.6-1.2 1.6a8 8 0 0 0 4.2 4.2l1.6-1.2 2.6 2.3-1.3 1.6C6.8 12.4 1.6 7.2 1.4 2.8z" fill="none" stroke="var(--orange)" stroke-width="1.2" stroke-linejoin="round"/></svg>
        <span>1300 555 218 (FREE TOLL )</span>
      </li>
      <li>
        <svg viewBox="0 0 14 14"><path d="M7 2c3.3 0 6 2 6 4.5S10.3 11 7 11c-.7 0-1.3-.1-1.9-.2L2 12.5l.9-2.6C1.7 9 1 7.8 1 6.5 1 4 3.7 2 7 2z" fill="none" stroke="var(--orange)" stroke-width="1.2" stroke-linejoin="round"/></svg>
        <span>+61 400 555 312</span>
      </li>
      <li>
        <svg viewBox="0 0 14 14"><rect x="1.5" y="3" width="11" height="8" fill="none" stroke="var(--orange)" stroke-width="1.2"/><path d="M1.5 3.5L7 8l5.5-4.5" fill="none" stroke="var(--orange)" stroke-width="1.2"/></svg>
        <span>support@halvenfx.com.au</span>
      </li>
    </ul>
  </footer>

  <div class="website">
    <span class="website-text">HALVENFX.COM.AU</span>
  </div>
</div>
</body>
</html>
```